依頼詳細
今回は、トップページデザインの募集になります。
レスポンシブデザインのサイトで、bootstrap4を利用しコーディングする予定になります。
デザイン幅は2000px、コンテンツの幅はbootstrap4デフォルトの1110pxを基準としてください。ただし最近のデザインの流行を取りいれて、フルワイドや、1200~15000px程度の幅のコンテンツをバランスよくレイアウトしてください。
コンテンツ配置は基本12分割になります。がデザインによっては、多少逸脱してもかまいません。
念のため、サンプルのPSDデータを添付しますので、参照ください。

本文のフォントはゴシック系は游ゴシック、メイリオ、明朝系は遊明朝でお願いします。
飾り文字はフリーフォントか、googleフォントを利用してください。

メイン画像部分・グローバルメニューは、ワイド適用でお願いします。

その他内容詳細に関しては、別添のExcel資料を参照してください。
不明点、質問などありましたらメッセージ等でご連絡ください。
ページ数
1ページ
希望イメージ
シンプル 複雑
単色 カラフル
暗い 明るい
日常 高級
遊び心 厳粛
未来的 伝統的
女性的 男性的
希望する色
黄・オレンジ系、グレー系
納品ファイル
• 高解像度JPG (.jpg)
• フォトショップ形式 (.psd)
補足説明
納品ファイルは、PDF及びクライアント表示確認用のJPGを準備お願いします。
※9月13日追記
本件クライアントのご提案選定に時間を要しておりまして、止むを得ず案件の期間を延長させていただきました。
デザイナー様各位にはご心配をお掛けしすみませんが、案件に問題はございませんのでご安心いただければと思います。
引き続き、どうぞ宜しくお願いいたします。

カラーや素材の入れ方が良かったです。

本件クライアントの確認に時間が掛かってしまいましたが、最終的にカラーや素材の使い方が良かったとのことで、kemo-riha様を当選とさせていただきました。
皆様ご提案ありがとうございました。
今後ともどうぞ宜しくお願いいたします。

```html
<!DOCTYPE html>
<html lang="ja">
<head>
<meta charset="utf-8">
<title>風原スポーツ｜レスリング用品専門店</title>
<link href="https://fonts.googleapis.com/css2?family=Noto+Sans+JP:wght@400;500;700;900&family=Oswald:wght@500;700&display=swap" rel="stylesheet">
<style>
:root{
  --orange:#f08a00;
  --orange-deep:#d96d00;
  --yellow:#f6c600;
  --ink:#222;
  --dark:#141414;
  --gray:#777;
  --line:#dcdcdc;
  --pale:#ececec;
  --red:#d8262b;
  --blue:#1f5fb8;
  --white:#fff;
}
*{box-sizing:border-box;margin:0;padding:0}
html,body{width:1200px;height:2536px;overflow:hidden}
body{font-family:"Noto Sans JP",sans-serif;color:var(--ink);background:var(--white);position:relative}
.en{font-family:"Oswald",sans-serif}

/* header */
.site-header{height:125px;background:linear-gradient(90deg,#0c0c0c,#262626 50%,#0c0c0c);position:relative;color:var(--white)}
.header-note{position:absolute;left:14px;top:3px;font-size:9px;color:#bbb}
.brand{position:absolute;left:36px;top:34px;display:flex;align-items:center;gap:10px}
.brand-mark{width:18px;height:18px;background:var(--orange)}
.brand-name{font-size:26px;font-weight:900;color:var(--orange);letter-spacing:1px;line-height:1}
.brand-sub{position:absolute;left:64px;top:66px;font-size:13px;font-weight:700;color:var(--orange);letter-spacing:3px}
.header-catch{position:absolute;left:300px;top:26px;width:600px;text-align:center;font-size:25px;font-weight:900;color:var(--yellow);line-height:1.45}
.header-tel{position:absolute;right:36px;top:22px;width:222px;border:2px solid var(--orange);padding:6px 10px;text-align:center}
.header-tel small{display:block;font-size:10px;color:#ddd}
.header-tel strong{display:flex;align-items:center;justify-content:center;gap:6px;font-size:26px;color:var(--white);line-height:1.2}
.header-tel span{display:block;font-size:10px;color:#ddd}

/* nav */
.global-nav{height:32px;background:var(--orange);display:flex;justify-content:center;align-items:center;gap:30px;font-size:13px;color:var(--white);font-weight:500}

/* search */
.search-row{height:40px;display:flex;justify-content:center;align-items:center;gap:8px;border-bottom:1px solid var(--line)}
.search-input{width:250px;height:24px;border:1px solid #bbb}
.search-btn{width:40px;height:24px;background:#333;color:var(--white);font-size:11px;display:flex;align-items:center;justify-content:center}
.welcome{margin-left:14px;font-size:11px;color:#555}

/* section heading */
.sec-title{text-align:center}
.sec-title h2{font-size:26px;font-weight:700;color:var(--orange)}
.sec-title p{font-size:12px;color:var(--gray);letter-spacing:1px}

/* news */
.news{height:780px;padding-top:36px}
.news-list{width:600px;margin:26px auto 0;border-top:1px solid var(--line)}
.news-item{display:flex;gap:14px;padding:16px 10px;border-bottom:1px solid var(--line)}
.news-date{width:70px;flex:none;font-size:10px;color:var(--gray)}
.news-thumb{width:90px;height:70px;flex:none;background:linear-gradient(135deg,#3a3a3a,#8a8a8a)}
.news-body{flex:1}
.news-body h3{font-size:12px;color:var(--orange);font-weight:700;margin-bottom:6px}
.news-body p{font-size:11px;color:#555;line-height:1.75}
.news-photo{width:170px;height:120px;flex:none;background:linear-gradient(135deg,#2b2f3a,#6d6f78 60%,#b9a27a)}
.more{display:block;width:130px;margin:22px auto 0;border:1px solid var(--orange);color:var(--orange);font-size:11px;text-align:center;padding:6px}

/* promo band */
.promo-band{height:460px;background:radial-gradient(ellipse at 50% 50%,rgba(240,138,0,.28),transparent 60%),linear-gradient(180deg,#dcdcdc,#f2f2f2 50%,#dcdcdc);padding-top:40px}
.promo-card{width:660px;margin:0 auto;background:var(--white);padding:16px 20px;box-shadow:0 2px 10px rgba(0,0,0,.12)}
.promo-head{background:var(--orange);color:var(--white);font-size:20px;font-weight:900;text-align:center;padding:6px}
.promo-head em{font-style:normal;color:var(--yellow)}
.promo-grid{display:flex;gap:10px;margin-top:14px}
.ph{background:linear-gradient(135deg,#c9ccd6,#8e97b5)}
.promo-suits{width:150px;height:170px;background:linear-gradient(90deg,#2a4fa0,#c8262b 50%,#2a4fa0)}
.promo-right{flex:1}
.promo-goods{display:flex;gap:8px}
.promo-goods div{flex:1;height:70px}
.promo-msg{font-size:14px;font-weight:700;line-height:1.6;margin-top:10px}
.promo-msg b{color:var(--red)}
.promo-order{display:flex;gap:12px;margin-top:14px;align-items:center}
.promo-order .shoe{width:130px;height:80px;background:linear-gradient(135deg,#1f3e8a,#e8e8f0)}
.promo-order h3{font-size:17px;font-weight:900;color:var(--blue)}
.promo-callout{background:var(--yellow);padding:8px 12px;font-size:14px;font-weight:900;text-align:center;flex:1}
.promo-callout small{display:block;font-size:10px;font-weight:400;margin-top:3px}

/* products */
.products{height:672px;padding-top:40px}
.product-list{display:flex;justify-content:center;gap:24px;margin-top:28px}
.card{width:200px;border:1px solid var(--line);position:relative}
.tag{position:absolute;left:0;top:0;padding:2px 10px;font-size:10px;color:var(--white);font-weight:700}
.tag.new{background:var(--red)}
.tag.sale{background:var(--orange)}
.card-img{height:200px;margin:24px 12px 10px}
.card-body{padding:0 12px 14px;font-size:10px;color:#555;line-height:1.7}
.card-body h3{font-size:12px;color:var(--ink);font-weight:700}
.price{font-size:16px;color:var(--red);font-weight:700}
.stars{color:var(--yellow);font-size:12px}

/* footer */
.site-footer{height:388px;background:radial-gradient(ellipse at 50% 40%,rgba(240,138,0,.35),transparent 55%),linear-gradient(180deg,#111,#1f1a14 50%,#111);color:var(--white);text-align:center;padding-top:34px}
.footer-lead{font-size:14px;font-weight:700}
.footer-brand{display:flex;justify-content:center;align-items:center;gap:24px;margin-top:18px}
.footer-brand .brand-name{font-size:28px}
.footer-brand .shop{font-size:34px;font-weight:900}
.footer-boxes{display:flex;justify-content:center;gap:20px;margin-top:22px}
.fbox{width:260px;border:2px solid var(--orange);padding:8px}
.fbox small{display:block;font-size:10px;color:#ddd}
.fbox strong{display:flex;align-items:center;justify-content:center;gap:6px;font-size:26px;line-height:1.2}
.fbox.ship strong{color:var(--orange)}
.footer-note{font-size:10px;color:#bbb;margin-top:12px}
.badges{display:flex;justify-content:center;gap:16px;margin-top:20px}
.badges span{width:90px;height:32px;background:#f0f0f0}
.copyright{height:36px;background:#222;color:#aaa;font-size:10px;display:flex;align-items:center;justify-content:center}
.to-top{position:absolute;right:24px;top:2454px;width:40px;height:40px;border-radius:50%;background:#eee;display:flex;align-items:center;justify-content:center}
</style>
</head>
<body>

<header class="site-header">
  <p class="header-note">大阪府内のレスリング専門店。レスリング用品は当店にお任せください。</p>
  <div class="brand"><span class="brand-mark"></span><span class="brand-name en">KAZAHARA</span></div>
  <p class="brand-sub en">WRESTLING</p>
  <p class="header-catch">小学生から有名選手まで幅広く対応可能！<br>各種商品２４時間ご注文受付！</p>
  <div class="header-tel">
    <small>お電話でのご注文・ご相談はこちら</small>
    <strong><svg width="18" height="18" viewBox="0 0 24 24"><path fill="#f08a00" d="M6.6 10.8a15 15 0 0 0 6.6 6.6l2.2-2.2c.3-.3.7-.4 1-.2 1.1.4 2.3.6 3.6.6.6 0 1 .4 1 1V20c0 .6-.4 1-1 1A17 17 0 0 1 3 4c0-.6.4-1 1-1h3.5c.6 0 1 .4 1 1 0 1.3.2 2.5.6 3.6.1.3 0 .7-.2 1z"/></svg>06-5550-0147</strong>
    <span>受付時間 9:00〜18:00</span>
  </div>
</header>

<nav class="global-nav">
  <span>ホーム</span><span>商品一覧</span><span>注文ガイド</span><span>お支払い・送品等について</span><span>新規会員登録</span><span>マイページ</span><span>会社概要</span><span>お問い合わせ</span><span>特定商取引法に基づく表記</span>
</nav>

<div class="search-row">
  <span class="search-input"></span><span class="search-btn">検索</span><span class="welcome">ようこそゲストさん</span>
</div>

<section class="news">
  <div class="sec-title"><h2>お知らせ</h2><p class="en">Information</p></div>
  <div class="news-list">
    <div class="news-item">
      <span class="news-date">2021.04.01</span>
      <div class="news-thumb" role="img" aria-label="新商品の写真"></div>
      <div class="news-body"><h3>新作スーツ入荷のお知らせ</h3><p>新作のレスリングスーツが入荷しました。サイズや色の種類も豊富にご用意しております。店頭でもオンラインでもお買い求めいただけます。ぜひこの機会にご覧ください。</p></div>
    </div>
    <div class="news-item">
      <span class="news-date">2021.03.15</span>
      <div class="news-thumb" role="img" aria-label="大会の写真"></div>
      <div class="news-body"><h3>大会協賛のお知らせ</h3><p>今年も地域のレスリング大会に協賛いたします。会場では特設ブースにて各種用品の販売を行います。選手の皆さまのご来場をお待ちしております。</p></div>
      <div class="news-photo" role="img" aria-label="試合中の選手の写真"></div>
    </div>
    <div class="news-item">
      <span class="news-date">2021.02.20</span>
      <div class="news-thumb" role="img" aria-label="店舗の写真"></div>
      <div class="news-body"><h3>営業時間変更のお知らせ</h3><p>誠に勝手ながら、当面の間営業時間を変更させていただきます。ご不便をおかけしますが、ご理解のほどよろしくお願いいたします。</p></div>
    </div>
    <div class="news-item">
      <span class="news-date">2021.01.10</span>
      <div class="news-body"><p>年始の配送スケジュールについてご案内します。</p></div>
    </div>
  </div>
  <span class="more">一覧を見る</span>
</section>

<section class="promo-band">
  <div class="promo-card">
    <p class="promo-head">レスリング関連商品は<em>当社</em>にお任せください。</p>
    <div class="promo-grid">
      <div class="promo-suits" role="img" aria-label="レスリングスーツの写真"></div>
      <div class="promo-right">
        <div class="promo-goods">
          <div class="ph" role="img" aria-label="シューズの写真"></div>
          <div class="ph" role="img" aria-label="サプリメントの写真"></div>
          <div class="ph" role="img" aria-label="計量器の写真"></div>
        </div>
        <p class="promo-msg">在庫商品全てを掲載しきれません！<br><b>未掲載商品</b>は、お気軽にお問い合わせください。</p>
      </div>
    </div>
    <div class="promo-order">
      <div class="shoe" role="img" aria-label="オーダーシューズの写真"></div>
      <h3>簡単注文のオーダースーツもございます！</h3>
      <div class="promo-callout">新素材ドライフレックスを採用。<small>吸汗性に優れ快適な着心地です。</small></div>
    </div>
  </div>
</section>

<section class="products">
  <div class="sec-title"><h2>オススメ商品</h2><p class="en">Featured Products</p></div>
  <div class="product-list">
    <div class="card"><span class="tag new">NEW</span>
      <div class="card-img" role="img" aria-label="ニーパッドの写真" style="background:linear-gradient(135deg,#222,#555)"></div>
      <div class="card-body"><p>商品番号：KP-0021</p><h3>ニーパッド ブラック</h3><p class="price">¥1,650</p><p class="stars">★★★☆☆</p></div>
    </div>
    <div class="card"><span class="tag sale">セール</span>
      <div class="card-img" role="img" aria-label="レスリングシューズの写真" style="background:linear-gradient(135deg,#1a1a1a,#4a4030)"></div>
      <div class="card-body"><p>商品番号：WS-1080</p><h3>レスリングシューズ<br>ブラック/ゴールド</h3><p class="price">¥4,990</p><p class="stars">★★★★☆</p></div>
    </div>
    <div class="card"><span class="tag sale">セール</span>
      <div class="card-img" role="img" aria-label="レスリングシューズの写真" style="background:linear-gradient(135deg,#1a1a1a,#4a4030)"></div>
      <div class="card-body"><p>商品番号：WS-1081</p><h3>レスリングシューズ<br>ブラック/シャンパン</h3><p class="price">¥4,990</p><p class="stars">★★★★☆</p></div>
    </div>
  </div>
</section>

<footer class="site-footer">
  <p class="footer-lead">レスリング商品専門店！ スーツ・シューズのオーダーも！</p>
  <div class="footer-brand"><span class="brand-mark"></span><span class="brand-name en">KAZAHARA</span><span class="shop">風原スポーツ</span></div>
  <div class="footer-boxes">
    <div class="fbox"><small>お電話でのご注文・ご相談はこちら</small><strong><svg width="20" height="20" viewBox="0 0 24 24"><path fill="#f08a00" d="M6.6 10.8a15 15 0 0 0 6.6 6.6l2.2-2.2c.3-.3.7-.4 1-.2 1.1.4 2.3.6 3.6.6.6 0 1 .4 1 1V20c0 .6-.4 1-1 1A17 17 0 0 1 3 4c0-.6.4-1 1-1h3.5c.6 0 1 .4 1 1 0 1.3.2 2.5.6 3.6.1.3 0 .7-.2 1z"/></svg>06-5550-0147</strong></div>
    <div class="fbox ship"><small>インターネットで24時間ご注文受付</small><strong>配送は全国対応</strong></div>
  </div>
  <p class="footer-note">各種メーカー商品を取り扱っております。お気軽にお問い合わせください。</p>
  <div class="badges"><span></span><span></span><span></span></div>
</footer>
<div class="copyright">© 2018-2021 KAZAHARA SPORTS</div>
<div class="to-top"><svg width="16" height="16" viewBox="0 0 16 16"><path d="M8 3 2 10h4v4h4v-4h4z" fill="#333"/></svg></div>

</body>
</html>
```